Business Card Design

our business is purchasing, rehabbing and flipping homes. Design a house in the palm of a hand. This card is for a new company based in Georgia. So we buy homes that have been foreclosed, short sales,abandond, old homes and vacant homes.
We help improve the communities that we work in. We would like to see designs that use a black background with green accent and other colors that blend and don't take away from the logo and other important information.

Industry/Entity Type

Business

Contact Information for Business Card

Hollow Pine Ventures
Turning Every Key Toward Home
2867 Ledgemoor Lane
Duluth GA 30096
Office: 678-555-0142
hollowpineventuresllc.example

```html
<!DOCTYPE html>
<html lang="en">
<head>
<meta charset="utf-8">
<title>Hollow Pine Ventures – Business Card</title>
<link rel="stylesheet" href="https://fonts.googleapis.com/css2?family=Cinzel:wght@400&family=Open+Sans:wght@400&family=Arimo:ital,wght@0,400;0,700;1,400;1,700&display=swap">
<style>
  :root {
    --backdrop: #c9c9c6;
    --card-black: #0c0c0c;
    --card-green: #147e4c;
    --ink-light: #e6e6e6;
    --ink-soft: #bdbdbd;
    --ink-white: #ffffff;
    --mark-green: #2aa86a;
  }
  html, body {
    margin: 0;
    width: 1200px;
    height: 807px;
    overflow: hidden;
    background: var(--backdrop);
  }
  .canvas {
    position: relative;
    width: 1200px;
    height: 807px;
  }
  .card {
    position: absolute;
    left: 130px;
    top: 145px;
    width: 940px;
    height: 537px;
    display: flex;
    flex-direction: column;
    box-shadow: 0 10px 30px rgba(0,0,0,0.25);
  }
  .card__brand {
    flex: 0 0 345px;
    background: var(--card-black);
    display: flex;
    flex-direction: column;
    align-items: center;
    justify-content: center;
    padding-top: 20px;
    box-sizing: border-box;
  }
  .brand__square {
    width: 30px;
    height: 30px;
    background: var(--mark-green);
    margin-bottom: 30px;
  }
  .brand__name {
    font-family: "Cinzel", serif;
    font-weight: 400;
    font-size: 33px;
    letter-spacing: 2px;
    color: var(--ink-light);
    margin: 0;
    line-height: 1;
  }
  .brand__tagline {
    font-family: "Open Sans", sans-serif;
    font-size: 19px;
    color: var(--ink-soft);
    margin: 10px 0 0;
  }
  .card__contact {
    flex: 1;
    background: var(--card-green);
    color: var(--ink-white);
    font-family: "Arimo", sans-serif;
    position: relative;
  }
  .contact__list {
    position: absolute;
    left: 70px;
    top: 62px;
    display: grid;
    grid-template-columns: 95px auto;
    row-gap: 8px;
    margin: 0;
    font-size: 19px;
    font-style: italic;
  }
  .contact__label {
    font-weight: 700;
  }
  .contact__value {
    margin: 0;
    font-weight: 400;
  }
  .contact__address {
    position: absolute;
    right: 75px;
    top: 78px;
    text-align: left;
    font-style: normal;
  }
  .address__company {
    font-weight: 700;
    font-size: 21px;
    letter-spacing: 0.3px;
    margin: 0 0 6px;
  }
  .address__line {
    font-size: 19px;
    margin: 0;
  }
</style>
</head>
<body>
<div class="canvas">
  <article class="card">
    <header class="card__brand">
      <div class="brand__square"></div>
      <h1 class="brand__name">HOLLOW PINE VENTURES</h1>
      <p class="brand__tagline">Turning Every Key Toward Home</p>
    </header>
    <section class="card__contact">
      <dl class="contact__list">
        <dt class="contact__label">Phone</dt>
        <dd class="contact__value">678-555-0142</dd>
        <dt class="contact__label">Website</dt>
        <dd class="contact__value">hollowpineventuresllc.example</dd>
      </dl>
      <address class="contact__address">
        <p class="address__company">HOLLOW PINE VENTURES</p>
        <p class="address__line">2867 Ledgemoor Lane Duluth GA 30096</p>
      </address>
    </section>
  </article>
</div>
</body>
</html>
```